Window Signage for Photocopy and Print Shop

We are based in Toronto and starting a photocopy, signage, banner, custom t-shirt, cups, passport photos, graphics business.

We need the following :-
1) window design that we can print and install. There are 2 -Windows size 55 "x 45" (See Photo of the building - Top 2 windows only). Need best colour combination to be visible from outside during day and night preferably. The graphics need to have dimension needed for printing vinyl and will be installed from outside.

We need the attached services to be included from the attached post-card (see attachments). Also include the services in addition to the post-card
photocopy, signage, banner, custom t-shirt, cups, passport photos, Roller banner, graphics business. It would be good to add other services a signage printing business can offer.

Make it Bright and mainly images. Put Text bold and readable for passing customers. Do not put our logo (just use it for colour inspiration and theme). Phone number big.

Must have different images (one for each window)

Contact details to include are

Dr. Kestrel - Sign & Print
Phone : 416 575 0198
website: www.drkestrel.ca

Target Market(s)

Signage and Printing

Industry/Entity Type

Signage and Graphics

Requirements
Must have
• Images of machines like - vinyl machine, photocopier. Images of Roller Banner, Exterior Signage) and products. TEXT READABLE for Make it Bright and mainly images. Put Text bold and readable for passing customers (preferably red background and white letters). Do not put our logo (just use it for colour inspiration and theme). Phone number big. Must have different images (one for each window)
Should not have
• copyrighted images

```html
<!DOCTYPE html>
<html lang="en">
<head>
<meta charset="utf-8">
<title>Dr. Kestrel - Sign &amp; Print — Window Signage</title>
<link rel="stylesheet" href="https://fonts.googleapis.com/css2?family=Montserrat:wght@800;900&family=Oswald:wght@500&family=Open+Sans:wght@700;800&family=Rubik:wght@700&display=swap">
<style>
  :root {
    --stage: #414141;
    --red: #e31b23;
    --red-deep: #b5121b;
    --red-dark: #8e0f16;
    --yellow: #ffec00;
    --white: #ffffff;
    --paper: #e9e9e9;
    --sky: #2fa9ee;
    --ink: #1b1b1b;
    --tick: #3fa6ec;
  }
  * { margin: 0; padding: 0; box-sizing: border-box; }
  html, body { width: 1200px; height: 786px; overflow: hidden; }
  body { background: var(--stage); position: relative; font-family: "Open Sans", sans-serif; }

  .window { position: absolute; top: 164px; width: 560px; height: 457px; overflow: hidden; }
  .window--left { left: 34px; background: var(--paper); }
  .window--right { left: 605px; background: linear-gradient(135deg, var(--red) 0%, var(--red-deep) 60%, var(--red) 100%); }

  .photo { position: absolute; border: 3px solid var(--white); }
  .photo--bare { border: none; }

  /* Left window */
  .left__red {
    position: absolute; inset: 0;
    background: linear-gradient(160deg, var(--red) 0%, var(--red-deep) 55%, var(--red) 100%);
    clip-path: polygon(245px 0, 560px 0, 560px 457px, 291px 457px);
  }
  .left__headline {
    position: absolute; left: 268px; top: 22px;
    font-family: "Montserrat", sans-serif; font-weight: 900;
    color: var(--yellow); font-size: 24.5px; line-height: 27px; letter-spacing: -0.2px;
  }
  .left__band {
    position: absolute; left: 256px; top: 119px; width: 304px; height: 48px;
    background: var(--white);
    clip-path: polygon(0 0, 100% 0, 100% 100%, 5px 100%);
    display: flex; align-items: center; justify-content: center;
    font-family: "Oswald", sans-serif; font-weight: 500; font-size: 31px;
    color: var(--red-dark); letter-spacing: -0.3px;
  }
  .service-list { position: absolute; left: 308px; top: 177px; list-style: none; }
  .service-list li {
    display: flex; align-items: center; height: 27px;
    color: var(--white); font-weight: 700; font-size: 22.5px; line-height: 1;
  }
  .service-list svg { width: 16px; height: 16px; margin-right: 5px; flex: none; }

  .left__footer {
    position: absolute; inset: 0; background: var(--sky);
    clip-path: polygon(0 364px, 284px 364px, 291px 457px, 0 457px);
  }
  .left__name {
    position: absolute; left: 10px; top: 352px; width: 260px; height: 23px;
    background: var(--red); color: var(--white);
    font-weight: 700; font-size: 14px; letter-spacing: 0.6px;
    display: flex; align-items: center; justify-content: center;
  }
  .left__contact {
    position: absolute; left: 0; top: 379px; width: 280px; text-align: center;
    font-weight: 800; font-size: 12px; color: var(--ink);
  }
  .phone {
    position: absolute; display: flex; align-items: center;
    font-family: "Rubik", sans-serif; font-weight: 700; color: var(--red);
    letter-spacing: -1px;
    text-shadow: 2px 0 0 #fff, -2px 0 0 #fff, 0 2px 0 #fff, 0 -2px 0 #fff, 1.5px 1.5px 0 #fff, -1.5px -1.5px 0 #fff, 1.5px -1.5px 0 #fff, -1.5px 1.5px 0 #fff;
  }
  .phone svg { flex: none; margin-right: 6px; }
  .left__phone { left: 16px; top: 392px; font-size: 33px; }
  .left__phone svg { width: 28px; height: 28px; }
  .left__web {
    position: absolute; left: 0; top: 432px; width: 280px; text-align: center;
    font-weight: 800; font-size: 15.5px; color: var(--ink); letter-spacing: 0.6px;
  }

  /* Right window */
  .right__header {
    position: absolute; left: 0; top: 0; width: 560px; height: 75px; background: var(--white);
    display: flex; align-items: center; justify-content: center; text-align: center;
    font-family: "Montserrat", sans-serif; font-weight: 900; color: var(--red);
    font-size: 28.5px; line-height: 29px; letter-spacing: -0.8px;
  }
  .right__band {
    position: absolute; left: 19px; top: 276px; width: 518px; height: 30px; background: var(--white);
    display: flex; align-items: center; justify-content: center;
    font-family: "Montserrat", sans-serif; font-weight: 900; font-size: 20px; color: var(--red); letter-spacing: 0.6px;
  }
  .service-line {
    position: absolute; left: 0; width: 560px; text-align: center;
    color: var(--white); font-weight: 700; font-size: 22.5px; line-height: 27px; white-space: nowrap;
  }
  .service-line .dot {
    display: inline-block; width: 9px; height: 9px; border-radius: 50%;
    background: var(--tick); margin: 0 6px; vertical-align: middle;
  }
  .right__footer { position: absolute; left: 0; top: 401px; width: 560px; height: 56px; background: var(--sky); }
  .right__name {
    position: absolute; left: 22px; top: 412px; width: 212px; text-align: center;
    font-family: "Montserrat", sans-serif; font-weight: 900; font-size: 14px; color: var(--ink); letter-spacing: -0.5px;
    text-shadow: 1px 0 0 #fff, -1px 0 0 #fff, 0 1px 0 #fff, 0 -1px 0 #fff;
  }
  .right__web {
    position: absolute; left: 22px; top: 430px; width: 212px; text-align: center;
    font-weight: 800; font-size: 12.5px; color: var(--ink); letter-spacing: 0.5px;
  }
  .right__phone { left: 276px; top: 409px; font-size: 33px; }
  .right__phone svg { width: 29px; height: 29px; }
</style>
</head>
<body>

<svg width="0" height="0" style="position:absolute" aria-hidden="true">
  <defs>
    <symbol id="icon-tick" viewBox="0 0 16 16">
      <path d="M2 8.5 L6.2 12.5 L14 3.5" fill="none" stroke="#3fa6ec" stroke-width="3.2" stroke-linecap="round" stroke-linejoin="round"/>
    </symbol>
    <symbol id="icon-phone" viewBox="0 0 30 30">
      <circle cx="15" cy="15" r="13.5" fill="#e31b23" stroke="#fff" stroke-width="2"/>
      <path d="M10.5 8.5c.8-.6 1.7-.4 2.1.3l1.4 2.4c.4.7.2 1.4-.4 1.9l-1 .8c.7 1.8 2 3.3 3.7 4.2l.9-1c.5-.6 1.3-.7 1.9-.3l2.3 1.5c.7.4.8 1.4.2 2.1l-1.1 1.2c-.8.9-2.2 1.1-3.5.5-3.6-1.6-6.4-4.6-7.7-8.3-.4-1.3-.1-2.6.8-3.4z" fill="#fff"/>
    </symbol>
  </defs>
</svg>

<section class="window window--left" aria-label="Left window design">
  <div class="photo" role="img" aria-label="Large-format printer printing a colourful banner" style="left:14px;top:13px;width:229px;height:103px;background:linear-gradient(120deg,#5a5f66 0%,#3a3d42 35%,#e05a2a 60%,#3aa860 80%,#2a6fc0 100%);"></div>
  <div class="photo" role="img" aria-label="Blue custom printed t-shirt" style="left:14px;top:124px;width:71px;height:94px;background:radial-gradient(circle at 50% 50%,#2a5fc4 0%,#2a5fc4 40%,#9fd3f0 70%);"></div>
  <div class="photo" role="img" aria-label="Custom photo printed mug" style="left:95px;top:124px;width:73px;height:94px;background:radial-gradient(circle at 50% 50%,#f2f2f2 0%,#d8d8d8 45%,#9fd3f0 72%);"></div>
  <div class="photo" role="img" aria-label="Roll-up banner stands" style="left:175px;top:124px;width:78px;height:94px;background:linear-gradient(90deg,#9fd3f0 0%,#f3f0c0 25%,#f0a040 60%,#9fd3f0 100%);"></div>
  <div class="photo" role="img" aria-label="Shop window poster graphics" style="left:14px;top:228px;width:115px;height:111px;background:linear-gradient(135deg,#2a2a2a 0%,#4d5f72 45%,#a9c6d6 100%);"></div>
  <div class="photo" role="img" aria-label="Wall of lettered exterior signs" style="left:138px;top:228px;width:127px;height:111px;background:linear-gradient(160deg,#3d3d3d 0%,#6b6258 50%,#2b2b2b 100%);"></div>

  <div class="left__red"></div>
  <h1 class="left__headline">ALL YOUR PRINT<br>AND SIGN SOLUTIONS<br>UNDER ONE ROOF</h1>
  <h2 class="left__band">WE ARE SPECIALIZED IN</h2>
  <ul class="service-list">
    <li><svg><use href="#icon-tick"/></svg>Post-card</li>
    <li><svg><use href="#icon-tick"/></svg>Photocopy</li>
    <li><svg><use href="#icon-tick"/></svg>Signage</li>
    <li><svg><use href="#icon-tick"/></svg>Banner</li>
    <li><svg><use href="#icon-tick"/></svg>Custom t-shirt</li>
    <li><svg><use href="#icon-tick"/></svg>Cups</li>
    <li><svg><use href="#icon-tick"/></svg>Passport photos</li>
    <li><svg><use href="#icon-tick"/></svg>Graphics business</li>
    <li><svg><use href="#icon-tick"/></svg>etc</li>
  </ul>

  <div class="left__footer"></div>
  <p class="left__name">DR. KESTREL - SIGN &amp; PRINT</p>
  <p class="left__contact">Contact us</p>
  <p class="phone left__phone"><svg><use href="#icon-phone"/></svg>416 575 0198</p>
  <p class="left__web">www.drkestrel.ca</p>
</section>

<section class="window window--right" aria-label="Right window design">
  <h1 class="right__header">ALL YOUR PRINT AND SIGN<br>SOLUTIONS UNDER ONE ROOF</h1>

  <div class="photo" role="img" aria-label="Storefront window graphics" style="left:20px;top:87px;width:175px;height:85px;background:linear-gradient(90deg,#3b3b3b 0%,#8a8a8a 40%,#e8e8e8 70%,#f5f5f5 100%);"></div>
  <div class="photo" role="img" aria-label="Illuminated channel-letter sign" style="left:201px;top:87px;width:103px;height:85px;background:radial-gradient(circle at 50% 45%,#6f8fbf 0%,#2c3e63 55%,#111a2c 100%);"></div>
  <div class="photo" role="img" aria-label="Black custom t-shirt mock-up" style="left:20px;top:177px;width:92px;height:88px;background:radial-gradient(circle at 50% 55%,#1d1d1d 0%,#2d2d2d 45%,#e6e6e6 80%);"></div>
  <div class="photo" role="img" aria-label="Passport photo service" style="left:117px;top:177px;width:91px;height:88px;background:linear-gradient(135deg,#f2f2f2 0%,#1e2a5c 35%,#263673 60%,#d9d9d9 100%);"></div>
  <div class="photo" role="img" aria-label="Roll-up banner stands" style="left:213px;top:177px;width:91px;height:88px;background:linear-gradient(90deg,#9aa4ad 0%,#d84a7a 25%,#f0a030 50%,#3a8ad0 75%,#9aa4ad 100%);"></div>
  <div class="photo photo--bare" role="img" aria-label="Wide-format vinyl printer with printed banner" style="left:313px;top:93px;width:232px;height:167px;border-radius:6px;background:linear-gradient(160deg,#d8d8dc 0%,#b9b9c0 35%,#2e5fa8 60%,#1f3c78 80%,#e05a2a 100%);"></div>

  <h2 class="right__band">WE ARE SPECIALIZED IN</h2>
  <p class="service-line" style="top:311px;">Post-card<span class="dot"></span>Photocopy<span class="dot"></span>Signage<span class="dot"></span>Banner</p>
  <p class="service-line" style="top:338px;">Custom t-shirt<span class="dot"></span>Cups<span class="dot"></span>Passport photos</p>
  <p class="service-line" style="top:365px;">Graphics business<span class="dot"></span>etc</p>

  <div class="right__footer"></div>
  <p class="right__name">DR. KESTREL - SIGN &amp; PRINT</p>
  <p class="right__web">www.drkestrel.ca</p>
  <p class="phone right__phone"><svg><use href="#icon-phone"/></svg>416 575 0198</p>
</section>

</body>
</html>
```